Simple, Professional and neat business card design for Vendralo Inc.

We're looking to re-vamp our business card design. We're a supplier of innovative feed ingredients for the North American animal agriculture industry. We are located in Lucknow, Ontario, Canada and our flagship product is a product that prevents milk fever in dairy cows when the calve, it is fed before calving and is very effective compared to other alternatives available on the market today.

Our company has Danish roots and we import all of our product from our Danish partner/manufacturer in Denmark. We like our design to embrace high professionalism while remaining neat and simple.

Target Market(s)

B2B, Feed Mills, Veterinary Clinics, Large integrators/producers,

Industry/Entity Type

Agribusiness

Contact Information for Business Card

We like the rounded corners because they make the card easy to sit in a wallet and not many use it so it makes the card stand out, just possibly something to take account for during the design.

As you can also see on the sliders below, looking for a that simple but proffesional scandinavian design.

Requirements
Nice to have
• Rounded corners
Should not have
• Too vibrant

```html
<!DOCTYPE html>
<html lang="en">
<head>
<meta charset="utf-8">
<title>Vendralo Inc. business card</title>
<link rel="stylesheet" href="https://fonts.googleapis.com/css2?family=Montserrat:wght@300;600;800&family=Open+Sans:wght@400;600;700&display=swap">
<style>
  :root {
    --bg: #3a3b3d;
    --navy: #1b2f86;
    --blue: #0e57a8;
    --gold: #c9a76a;
    --cream: #f4eedf;
    --mist: #e6ebee;
    --white: #ffffff;
  }
  * { box-sizing: border-box; margin: 0; padding: 0; }
  html, body { width: 1200px; height: 974px; overflow: hidden; }
  body {
    background: var(--bg);
    font-family: "Open Sans", sans-serif;
    position: relative;
  }
  .card {
    position: absolute;
    width: 520px;
    height: 300px;
    border-radius: 28px;
    overflow: hidden;
    background: var(--cream);
    box-shadow: 0 10px 30px rgba(0,0,0,.35);
  }
  .card-back { left: 70px; top: 110px; }
  .card-front { left: 610px; top: 540px; }
  .texture {
    position: absolute; inset: 0;
    background: radial-gradient(ellipse at 70% 40%, #eef1f2 0%, #f1ecdf 55%, #ece2cc 100%);
  }
  .tagline {
    position: absolute; left: 0; right: 0; top: 34px;
    text-align: center;
    font-family: "Open Sans", sans-serif;
    font-weight: 700; font-size: 14px; letter-spacing: .6px;
    color: var(--navy); line-height: 1.35;
    text-transform: uppercase;
  }
  .features {
    position: absolute; left: 30px; right: 30px; top: 92px;
    display: flex; justify-content: space-around;
  }
  .feature { width: 140px; text-align: center; }
  .feature svg { width: 70px; height: 70px; display: block; margin: 0 auto 8px; }
  .feature-label { font-size: 13px; letter-spacing: .6px; color: #333; }
  .brand {
    font-family: "Montserrat", sans-serif;
    font-weight: 800; color: var(--blue);
    text-transform: uppercase;
    display: flex; align-items: center; gap: 12px;
  }
  .brand-dot { width: 26px; height: 26px; border-radius: 50%; background: var(--blue); }
  .card-back .brand { position: absolute; left: 0; right: 0; bottom: 30px; justify-content: center; font-size: 30px; }
  .card-front .brand { position: absolute; left: 30px; top: 130px; font-size: 28px; }
  .person {
    position: absolute; right: 30px; top: 34px; text-align: right;
    font-family: "Montserrat", sans-serif; font-size: 24px; color: var(--navy);
    text-transform: uppercase; padding-bottom: 6px; border-bottom: 1px solid var(--navy);
  }
  .person .first { font-weight: 600; }
  .person .last { font-weight: 300; }
  .address {
    position: absolute; right: 30px; top: 86px; text-align: center;
    font-size: 12px; font-weight: 700; color: var(--navy); line-height: 1.4;
  }
  .address svg { display: block; margin: 0 auto 4px; width: 16px; height: 20px; }
  .band {
    position: absolute; left: 0; right: 0; bottom: 0; height: 112px;
    background: var(--blue); border-top: 5px solid var(--gold);
    display: flex; align-items: center; justify-content: space-around;
    color: var(--white); font-size: 12.5px; letter-spacing: .4px;
  }
  .band .col { display: flex; flex-direction: column; gap: 8px; padding: 0 14px; }
  .band .col + .col { border-left: 1px solid rgba(255,255,255,.35); }
  .band .row { display: flex; align-items: center; gap: 8px; }
  .band svg { width: 12px; height: 12px; fill: var(--white); }
</style>
</head>
<body>

<section class="card card-back">
  <div class="texture" role="img" aria-label="Soft cream background with faint light rays over fields"></div>
  <p class="tagline">Distributor of innovative feed ingredients<br>and other preventative health products.</p>
  <div class="features">
    <div class="feature">
      <svg viewBox="0 0 70 70" aria-hidden="true">
        <path d="M35 6 L60 15 V34 C60 50 48 60 35 65 C22 60 10 50 10 34 V15 Z" fill="var(--blue)" stroke="var(--navy)" stroke-width="3"/>
        <circle cx="35" cy="34" r="12" fill="var(--white)"/>
        <path d="M35 28 V40 M29 34 H41" stroke="var(--navy)" stroke-width="3"/>
      </svg>
      <div class="feature-label">Preventative Care</div>
    </div>
    <div class="feature">
      <svg viewBox="0 0 70 70" aria-hidden="true">
        <path d="M14 52 A26 26 0 1 1 52 58" fill="none" stroke="var(--navy)" stroke-width="5" stroke-dasharray="4 5"/>
        <path d="M35 35 L32 14 L38 14 Z" fill="var(--navy)"/>
        <path d="M30 56 L42 40 L48 48 L62 28" fill="none" stroke="var(--blue)" stroke-width="6"/>
        <path d="M55 26 L65 24 L63 34 Z" fill="var(--blue)"/>
      </svg>
      <div class="feature-label">High-performance</div>
    </div>
    <div class="feature">
      <svg viewBox="0 0 70 70" aria-hidden="true">
        <circle cx="35" cy="35" r="30" fill="var(--blue)" stroke="var(--navy)" stroke-width="4"/>
        <text x="35" y="45" text-anchor="middle" font-family="Open Sans, sans-serif" font-weight="700" font-size="28" fill="var(--white)">Rx</text>
        <path d="M50 12 L20 58" stroke="var(--navy)" stroke-width="4"/>
      </svg>
      <div class="feature-label">Prescription-free</div>
    </div>
  </div>
  <div class="brand"><span class="brand-dot"></span>Vendralo Inc.</div>
</section>

<section class="card card-front">
  <div class="texture" role="img" aria-label="Soft cream background with faint light rays over fields"></div>
  <div class="brand"><span class="brand-dot"></span>Vendralo Inc.</div>
  <div class="person"><span class="first">Mikkel</span> <span class="last">Sorensen</span></div>
  <div class="address">
    <svg viewBox="0 0 16 20" aria-hidden="true"><path d="M8 0 C3.5 0 0 3.5 0 8 C0 13 8 20 8 20 C8 20 16 13 16 8 C16 3.5 12.5 0 8 0 Z" fill="var(--gold)"/><circle cx="8" cy="8" r="3" fill="var(--blue)"/></svg>
    Box 412, Brindlewood,<br>Ontario Canada N0X 4K0
  </div>
  <div class="band">
    <div class="col">
      <div class="row"><svg viewBox="0 0 12 12" aria-hidden="true"><path d="M0 2 H12 V10 H0 Z M0 2 L6 7 L12 2" stroke="var(--blue)" stroke-width="1"/></svg>mikkel@vendralo.com</div>
      <div class="row"><svg viewBox="0 0 12 12" aria-hidden="true"><circle cx="6" cy="6" r="6"/></svg>www.vendralo.com</div>
    </div>
    <div class="col">
      <div class="row"><svg viewBox="0 0 12 12" aria-hidden="true"><path d="M2 0 L5 3 L3.5 5 C4.5 7 5 7.5 7 8.5 L9 7 L12 10 L10 12 C4 11 1 8 0 2 Z"/></svg>555-214-0388</div>
      <div class="row"><svg viewBox="0 0 12 12" aria-hidden="true"><path d="M0 5 C3 1 9 1 12 5 L10 6 L8 4 H4 L2 6 Z M2 8 H10 V11 H2 Z"/></svg>555-214-5871</div>
    </div>
    <div class="col">
      <div class="row"><svg viewBox="0 0 12 12" aria-hidden="true"><path d="M2 0 L5 3 L3.5 5 C4.5 7 5 7.5 7 8.5 L9 7 L12 10 L10 12 C4 11 1 8 0 2 Z"/></svg>888-555-0142</div>
      <div class="row"><svg viewBox="0 0 12 12" aria-hidden="true"><path d="M1 4 H11 V11 H1 Z M3 0 H9 V4 H3 Z"/></svg>555-214-5990</div>
    </div>
  </div>
</section>

</body>
</html>
```